Garlic Farm for Farm Sales/Restaurant sales

Need a professional, but appealing to agriculture world. We are selling 27 kinds of Organic Garlic from a farm in Simla,CO. I have uploaded logo and business information-we are going to need a template, because I will need to use it for four separate people.
-We are trying to appeal to Farm to table restaurants
-As well as growers/farmers

Target Market(s)

Agriculture Sales/Restaurants-Organic

Industry/Entity Type

Agriculture

Contact Information for Business Card

Want it to look more unique then your average orbel mart card- I want it to look amazing

Font styles to use
Sans Serif

Colors
0455a3
ec1f27
fbed22
ffffff

Requirements
Must have
• Just be creative
Nice to have
• Colorful
Should not have
• plain

```html
<!DOCTYPE html>
<html lang="en">
<head>
<meta charset="utf-8">
<title>Plainsview Garlic Co – Business Card</title>
<link rel="stylesheet" href="https://fonts.googleapis.com/css2?family=Cabin:wght@400;600&family=Cinzel:wght@400;600&display=swap">
<style>
  :root {
    --bg: #ebe7e0;
    --card-white: #ffffff;
    --sun-yellow: #f6d319;
    --chili-red: #b01d24;
    --text-red: #c8323a;
    --ink-navy: #2b2f63;
    --brand-blue: #1f3f94;
    --shadow: rgba(40, 30, 20, 0.18);
  }
  * { box-sizing: border-box; margin: 0; padding: 0; }
  html, body { width: 1200px; height: 892px; overflow: hidden; background: var(--bg); }
  .stage {
    width: 1200px; height: 892px;
    display: flex; align-items: center; justify-content: center; gap: 90px;
  }
  .card {
    position: relative;
    width: 360px; height: 630px;
    background: var(--card-white);
    box-shadow: 0 10px 28px var(--shadow);
    overflow: hidden;
  }
  .card-front .color-blocks { position: absolute; inset: 0; }
  .front-content {
    position: absolute; left: 0; right: 0; top: 276px;
    display: flex; flex-direction: column; align-items: center;
    text-align: center;
  }
  .brand-dot {
    display: block;
    width: 30px; height: 30px; border-radius: 50%;
    background: var(--chili-red);
    margin-bottom: 14px;
  }
  .brand-name {
    font-family: "Cabin", sans-serif; font-weight: 600;
    font-size: 23px; line-height: 1.2; color: var(--ink-navy); letter-spacing: 0.5px;
    margin-bottom: 16px;
  }
  .person-name {
    font-family: "Cinzel", serif; font-weight: 400;
    font-size: 24px; color: var(--text-red); letter-spacing: 1px;
    margin-bottom: 12px;
  }
  .contact {
    font-family: "Cabin", sans-serif; font-size: 17px;
    color: var(--text-red); line-height: 1.55;
  }
  .card-back {
    display: flex; flex-direction: column; align-items: center; justify-content: center;
    background: linear-gradient(180deg, #ffffff 0%, #f1f1f1 100%);
  }
  .back-title {
    font-family: "Cinzel", serif; font-weight: 400;
    font-size: 46px; color: var(--brand-blue); letter-spacing: 3px; line-height: 1;
  }
  .back-subtitle {
    font-family: "Cabin", sans-serif; font-weight: 400;
    font-size: 17px; color: var(--text-red); letter-spacing: 4px;
    margin-top: 10px; margin-bottom: 34px;
  }
  .back-mark {
    width: 70px; height: 70px; border-radius: 50%;
    background: var(--chili-red);
  }
</style>
</head>
<body>
<main class="stage">
  <section class="card card-front" aria-label="Card front">
    <svg class="color-blocks" width="360" height="630" viewBox="0 0 360 630" aria-hidden="true">
      <polygon points="0,0 180,0 180,258 0,435" fill="var(--sun-yellow)"/>
      <polygon points="180,0 360,0 360,435 180,258" fill="var(--chili-red)"/>
    </svg>
    <div class="front-content">
      <span class="brand-dot"></span>
      <p class="brand-name">Plainsview<br>Garlic Co</p>
      <p class="person-name">Dana Ortiz</p>
      <p class="contact">5550100199</p>
      <p class="contact">VP 742 Prairie Row Simla,<br>CO 80835</p>
    </div>
  </section>

  <section class="card card-back" aria-label="Card back">
    <p class="back-title">PLAINSVIEW</p>
    <p class="back-subtitle">GARLIC CO</p>
    <span class="back-mark"></span>
  </section>
</main>
</body>
</html>
```